Marcus Pellow Carpentry & Joinery

Hello, I would like a flyer designed for my new business doing small projects in my local area for home-owners. I am a professional tradesman.
The type of work I am offering is:
- decks/decking
- external stairs & railings
- install windows & doors
- roofs & gutters
- small additions
- built-in wardrobes
- finish work
- demolition

It would be great if the flyer could mention these, or use phrasing that fits this kind of construction work.
My idea for a slogan was "new work and repairs to any age home".

Please also mention FREE QUOTES and have my email and phone number included on the flyer, along with my carpentry licence number, which I can provided.

I'd like a one page, single-sided flyer that could be printed as DL.
Colour and style is up to you! I'll be placing this flyer on counters & in the windows of local businesses, so something simple and eye-catching is preferred.

Thank you!

```html
<!DOCTYPE html>
<html lang="en">
<head>
<meta charset="utf-8">
<title>Marcus Pellow Carpentry &amp; Joinery – Flyer</title>
<link rel="stylesheet" href="https://fonts.googleapis.com/css2?family=Source+Sans+3:wght@400;600;700&family=Roboto+Condensed:wght@300;400;700&display=swap">
<style>
  :root {
    --stage: #1b1b1b;
    --paper: #ffffff;
    --maroon: #7b1a37;
    --yellow: #fdd20b;
    --amber: #f9b233;
    --ink: #1e1e1e;
    --mist: #e9e6e3;
  }
  * { margin: 0; padding: 0; box-sizing: border-box; }
  html, body { width: 1200px; height: 1000px; overflow: hidden; background: var(--stage); }
  .flyer {
    position: absolute; left: 303px; top: 112px; width: 585px; height: 758px;
    background: var(--paper); overflow: hidden;
    font-family: "Source Sans 3", "Myriad Pro", sans-serif;
  }
  .flyer-shapes { position: absolute; inset: 0; }
  .headline {
    position: absolute; left: 19px; top: 30px; color: var(--ink);
    font-size: 35px; line-height: 43px; font-weight: 400; letter-spacing: -0.3px;
  }
  .headline strong { font-weight: 700; }
  .services-title {
    position: absolute; left: 15px; top: 208px; width: 270px; height: 26px;
    background: var(--yellow); border-radius: 2px;
    color: #3a1a12; font-weight: 700; font-size: 13.5px; line-height: 26px; padding-left: 15px;
  }
  .services { list-style: none; position: absolute; left: 15px; top: 248px; }
  .services li {
    height: 26px; margin-bottom: 14.7px; padding-left: 30px; position: relative;
    color: #fff; font-weight: 700; font-size: 14.5px; line-height: 26px; letter-spacing: 0.1px;
  }
  .services li::before {
    content: ""; position: absolute; left: 9px; top: 7px; width: 5px; height: 10px;
    border: solid #fff; border-width: 0 3px 3px 0; transform: rotate(40deg);
  }
  .licence {
    position: absolute; left: 55px; top: 693px; width: 125px; text-align: center;
    font-family: "Roboto Condensed", sans-serif; color: #fff;
  }
  .licence-label { font-size: 18px; font-weight: 300; line-height: 22px; }
  .licence-number {
    margin-top: 3px; background: var(--yellow); color: var(--ink); border-radius: 3px;
    font-weight: 700; font-size: 18px; letter-spacing: 6px; line-height: 24px; padding-left: 5px;
  }
  .contact {
    position: absolute; left: 290px; top: 614px; width: 268px; text-align: center;
    font-family: "Roboto Condensed", sans-serif; color: #fff;
  }
  .free-quotes { color: var(--yellow); font-weight: 700; font-size: 25px; line-height: 30px; }
  .phone { font-weight: 300; font-size: 42px; line-height: 48px; letter-spacing: 1.5px; margin-top: 4px; }
  .divider { border-top: 1px dashed rgba(255,255,255,.8); margin: 6px 15px 0 14px; }
  .email { font-size: 18px; font-weight: 400; letter-spacing: .5px; margin-top: 7px; }
  .quote-arrow { position: absolute; top: 6px; }
</style>
</head>
<body>
<main class="flyer">
  <svg class="flyer-shapes" width="585" height="758" viewBox="0 0 585 758" aria-hidden="true">
    <defs>
      <linearGradient id="sunWash" x1="0" y1="0" x2="0.3" y2="1">
        <stop offset="0" stop-color="#f9b233"/>
        <stop offset="0.35" stop-color="#fde7a6"/>
        <stop offset="1" stop-color="#ffffff"/>
      </linearGradient>
    </defs>
    <rect width="585" height="330" fill="url(#sunWash)"/>
    <rect x="0" y="300" width="585" height="40" fill="#fff"/>
    <g fill="var(--maroon)">
      <rect x="15" y="248" width="560" height="26" rx="2"/>
      <rect x="15" y="288.7" width="560" height="26" rx="2"/>
      <rect x="15" y="329.4" width="560" height="26" rx="2"/>
      <rect x="15" y="370.1" width="560" height="26" rx="2"/>
      <rect x="15" y="410.8" width="560" height="26" rx="2"/>
      <rect x="15" y="451.5" width="560" height="26" rx="2"/>
      <rect x="15" y="492.2" width="560" height="26" rx="2"/>
      <rect x="15" y="532.9" width="555" height="26" rx="2"/>
    </g>
  </svg>

  <svg class="flyer-shapes" width="585" height="758" viewBox="0 0 585 758">
    <defs>
      <linearGradient id="photoTone" x1="0" y1="0" x2="0" y2="1">
        <stop offset="0" stop-color="#e9c98a"/>
        <stop offset="0.3" stop-color="#9c8a5a"/>
        <stop offset="0.5" stop-color="#3f6e60"/>
        <stop offset="0.7" stop-color="#3a1d22"/>
        <stop offset="1" stop-color="#1e0c10"/>
      </linearGradient>
    </defs>
    <path d="M312 0 C266 140 290 370 585 572 L585 0 Z" fill="#fff"/>
    <path d="M330 0 C288 140 312 360 585 520 L585 0 Z" fill="url(#photoTone)"
          role="img" aria-label="Photo of a small green model house with white trim and an orange tiled roof"/>
    <path d="M0 640 C70 622 180 626 250 646 L0 680 Z" fill="var(--yellow)"/>
    <path d="M0 634 C120 618 210 650 290 652 C390 652 470 566 585 574 L585 600 C470 592 390 670 290 670 C210 668 120 640 0 650 Z" fill="var(--mist)"/>
    <path d="M0 646 C120 630 210 662 290 664 C390 664 470 590 585 598 L585 758 L0 758 Z" fill="var(--maroon)"/>
  </svg>

  <h1 class="headline">New <strong>Work</strong><br>and <strong>Repairs</strong><br>to any age <strong>Home</strong></h1>

  <div class="services-title">THE TYPE OF WORK I AM OFFERING IS:</div>
  <ul class="services">
    <li>DECKS/DECKING</li>
    <li>EXTERNAL STAIRS &amp; RAILINGS</li>
    <li>INSTALL WINDOWS &amp; DOORS</li>
    <li>ROOFS &amp; GUTTERS</li>
    <li>SMALL ADDITIONS</li>
    <li>BUILT-IN WARDROBES</li>
    <li>FINISH WORK</li>
    <li>DEMOLITION</li>
  </ul>

  <div class="licence">
    <div class="licence-label">Licence Number:</div>
    <div class="licence-number">4870153</div>
  </div>

  <div class="contact">
    <svg class="quote-arrow" style="left:38px" width="30" height="32" viewBox="0 0 30 32" aria-hidden="true">
      <path d="M27 3 C12 6 5 15 5 28 M1 22 L5 29 L10 23" fill="none" stroke="#fff" stroke-width="1.5"/>
    </svg>
    <svg class="quote-arrow" style="right:36px" width="30" height="32" viewBox="0 0 30 32" aria-hidden="true">
      <path d="M3 3 C18 6 25 15 25 28 M20 23 L25 29 L29 22" fill="none" stroke="#fff" stroke-width="1.5"/>
    </svg>
    <div class="free-quotes">FREE QUOTES</div>
    <div class="phone">0400 555-182</div>
    <div class="divider"></div>
    <div class="email">marcuspellow@mailbox.com</div>
  </div>
</main>
</body>
</html>
```